Bench Advertisement - We Buy Houses Design Needed

Need a catchy, simple but elegant design for bus benches to advertise our company.

We need our website, or phone number, and a smal description (1-2 bulletpoints of what we do and what we offer)

The tricky part is for the designer to fit everything and make the website name as part of the title and fitting everything so that people passing by on the street can see what we offer.

Our website is quickhomeofferhub.com - (916) 555-0142

Something simple but something that catches the eye of walking pedestrians, and drivers driving by the bench.

Our company buys houses, any condition, any situation, we buy houses for cash and close quickly. You can use this description to create a few bulletpoints however you like. Must follow dimensions in attachment.

Target Market(s)

People in foreclosure, about to lose their homes, people that need a quick cash sale of their property

Industry/Entity Type

Real Estate

Requirements
Must have
• catchy, website name, phone number, few brief bulletpoints about what we offer, colors that will catch peoples eye while walking or driving - advertisement will be placed on bus benches - visit our website to see the type of houses we buy - Also have more work for winner of design with possible bonuses
Nice to have
• Feel free to use description or images on our website - make sure the description is just bullet points and it fits with the overall theme / size of the advertisement - Bold bright colors - put yourself in their shoes (if you were going through financial difficulties and about to lose your house to foreclosure or auction, what would you want to see to pick up the phone and call us for a quick sale of your house?) (or if you have a house that you are having a problem with, problem renters, unkept/beat up house, what would make you want to call us and sell your house to us?)

```html
<!DOCTYPE html>
<html lang="en">
<head>
<meta charset="utf-8">
<title>Quick Home Offer Hub – Bench Advertisement</title>
<link rel="stylesheet" href="https://fonts.googleapis.com/css2?family=Montserrat:wght@500;600;700;800&display=swap">
<style>
  :root {
    --page-bg: #eef0f2;
    --frame: #9aa2a9;
    --blue-deep: #15549f;
    --blue-mid: #1d6cc0;
    --blue-light: #2a7fd2;
    --gold: #f6c21c;
    --band: #f0b317;
    --band-edge: #f7c93a;
    --white: #ffffff;
  }
  * { margin: 0; padding: 0; box-sizing: border-box; }
  html, body {
    width: 1200px;
    height: 827px;
    overflow: hidden;
    background: var(--page-bg);
    font-family: "Montserrat", Arial, sans-serif;
  }
  .bench-ad {
    position: absolute;
    left: 40px;
    top: 238px;
    width: 1120px;
    height: 350px;
    border: 5px solid var(--frame);
    background: radial-gradient(ellipse at 45% 40%, var(--blue-light) 0%, var(--blue-mid) 45%, var(--blue-deep) 100%);
    color: var(--white);
    overflow: hidden;
  }
  .welcome {
    position: absolute;
    left: 45px;
    top: 46px;
    font-size: 23px;
    font-weight: 600;
    letter-spacing: 0.5px;
  }
  .headline {
    position: absolute;
    left: 45px;
    top: 78px;
    font-size: 37px;
    font-weight: 800;
    color: var(--gold);
    letter-spacing: 0.3px;
  }
  .services {
    position: absolute;
    left: 45px;
    top: 132px;
    display: flex;
    gap: 14px;
    list-style: none;
    font-size: 21px;
    font-weight: 700;
    letter-spacing: 0.6px;
  }
  .services li::before { content: "• "; }
  .brand-name {
    position: absolute;
    left: 785px;
    top: 142px;
    width: 300px;
    text-align: center;
    font-size: 20px;
    font-weight: 700;
    letter-spacing: 0.2px;
  }
  .call {
    position: absolute;
    left: 50px;
    top: 243px;
    font-size: 25px;
    font-weight: 700;
  }
  .call .number { margin-left: 14px; }
  .tagline {
    position: absolute;
    right: 38px;
    top: 243px;
    font-size: 26px;
    font-weight: 800;
    letter-spacing: 0.3px;
  }
  .web-band {
    position: absolute;
    left: 0;
    bottom: 0;
    width: 100%;
    height: 52px;
    background: linear-gradient(90deg, var(--band) 0%, var(--band-edge) 50%, var(--band) 100%);
    display: flex;
    align-items: center;
    justify-content: center;
    font-size: 16px;
    font-weight: 700;
    letter-spacing: 2.6px;
    text-transform: uppercase;
  }
</style>
</head>
<body>
  <section class="bench-ad" aria-label="Bench advertisement">
    <p class="welcome">WELCOME TO</p>
    <h1 class="headline">QUICK HOME OFFER HUB</h1>
    <ul class="services">
      <li>WE BUY</li>
      <li>WE BUILD</li>
      <li>WE SELL</li>
    </ul>
    <p class="brand-name">QUICK HOME OFFER HUB</p>
    <p class="call">Call Us Now:<span class="number">(916) 555-0142</span></p>
    <p class="tagline">THE ONLY SOLUTION TO EVERY SITUATION.</p>
    <p class="web-band">Visit our website today : www.quickhomeofferhub.com</p>
  </section>
</body>
</html>
```